Progress bar toward 1 Million goal (horizontal)

We are a group of volunteers working to elect Democrats in the US. We are a chapter of a national group called Tide Rally, and our name is Forward Bay Circle. We attempt to follow the Tide Rally style guide. In 2022, we are running a campaign including thousands of volunteers to write 1 million physical, sent through the National Parcel Bureau, paper letters to prospective voters ahead of the 2022 elections. We need a thermometer-type graphic to visually illustrate in our newsletter and on our website our progress towards that goal. Here is our website: https://www.forwardbaycirclenotes.org which was built to facilitate that goal. Here are the Tide Rally style guidelines: https://tiderally.org/p/brand. A design involving an evocative receptacle filling with letters is an obvious possibility. A horizontal design would work better on our website and in our newsletter. These are pre-printed physical letters being sent to likely Democratic voters, with a small section handwritten by a volunteer. The envelopes are also hand-addressed by the volunteer. You may see a letter example and instructions to letter-writing volunteers here: https://ballotpenpals.org/instructions. All the letters are held until late October and mailed on the same date.

Target Market(s)

Activist progressive volunteers mostly 60+

Industry/Entity Type

Progressive activism. Our website: www.forwardbaycirclenotes.org

Font styles to use
Sans Serif

Colors

Designer to choose colors to be used in the design.

Requirements
Must have
• Horizontal orientation; use Tide Rally style guide for colors and fonts; theme involving envelopes; postage; National parcel bureau; mailboxes etc.
Nice to have
• conveys motion; progress, and design can be adjusted to "fill in" as we reach the 1 Million goal

```html
<!DOCTYPE html>
<html lang="en">
<head>
<meta charset="utf-8">
<title>Tide Rally – 1000 Letters Progress</title>
<link rel="stylesheet" href="https://fonts.googleapis.com/css2?family=Alfa+Slab+One&family=Bree+Serif&family=Oswald:wght@700&family=Yellowtail&display=swap">
<style>
  :root{
    --navy:#03264f;
    --sky:#00c0ff;
    --yellow:#fdfd25;
    --white:#ffffff;
    --grey:#e6e6e6;
    --coral:#fb5a66;
    --envelope:#eef0f4;
    --star-light:rgba(170,225,255,.35);
    --star-dark:rgba(120,150,190,.25);
    --star-pale:rgba(255,255,255,.35);
  }
  *{box-sizing:border-box;margin:0;padding:0}
  html,body{width:818px;height:1200px;overflow:hidden;background:var(--white)}
  .canvas{width:818px;height:1200px;display:flex;flex-direction:column}
  .panel{position:relative;height:300px;overflow:hidden;background:var(--bg)}
  .panel--white{--bg:var(--white);--script:var(--sky);--top:var(--grey);--base:var(--navy);--split:57%;--word:var(--coral);--track:var(--grey);--fill:var(--navy);--count:var(--navy);--brand:var(--coral);--stars:var(--star-light)}
  .panel--navy{--bg:var(--navy);--script:var(--yellow);--top:var(--white);--base:var(--sky);--split:53%;--word:var(--yellow);--track:var(--white);--fill:var(--sky);--count:var(--sky);--brand:var(--coral);--stars:var(--star-dark)}
  .panel--sky{--bg:var(--sky);--script:var(--navy);--top:var(--white);--base:var(--navy);--split:40%;--word:var(--navy);--track:var(--white);--fill:var(--navy);--count:var(--navy);--brand:var(--white);--stars:var(--star-pale)}
  .panel--yellow{--bg:var(--yellow);--script:var(--coral);--top:var(--white);--base:var(--navy);--split:36%;--word:var(--navy);--track:var(--white);--fill:var(--navy);--count:var(--navy);--brand:var(--coral);--stars:var(--star-pale)}

  .star-band{position:absolute;left:30px;right:30px;height:18px;border-radius:9px;background:var(--stars)}
  .star-band--top{top:12px}
  .star-band--bottom{top:270px}

  .brand{position:absolute;left:667px;top:50px;font-family:"Bree Serif",serif;font-size:22px;color:var(--brand)}

  .invite{position:absolute;left:0;width:818px;top:58px;text-align:center;padding-right:10px;font-family:"Yellowtail",cursive;font-size:34px;color:var(--script);z-index:2;line-height:1}
  .goal{position:absolute;left:272px;top:72px;font-family:"Alfa Slab One",serif;font-size:132px;line-height:1;letter-spacing:-2px;
    background:linear-gradient(to bottom,var(--top) 0 var(--split),var(--base) var(--split) 100%);
    -webkit-background-clip:text;background-clip:text;color:transparent}
  .goal-unit{position:absolute;left:418px;top:182px;font-family:"Bree Serif",serif;font-size:27px;letter-spacing:2px;color:var(--word)}

  .tracker{position:absolute;left:160px;top:226px;width:512px;height:11px;border-radius:6px;background:var(--track)}
  .tracker-fill{position:absolute;left:0;top:0;height:100%;width:var(--progress);border-radius:6px;background:var(--fill)}
  .tracker-marker{position:absolute;top:-8px;left:calc(var(--progress) - 2px);width:38px;height:24px}
  .tracker-count{position:absolute;top:14px;left:calc(var(--progress) + 20px);font-family:"Oswald",sans-serif;font-weight:700;font-size:13px;color:var(--count)}
  .panel--navy .tracker-count{font-size:19px;top:12px;left:calc(var(--progress) + 1px)}
</style>
</head>
<body>
<main class="canvas">

  <section class="panel panel--white" style="--progress:20%">
    <div class="star-band star-band--top" role="img" aria-label="Row of pale stars"></div>
    <p class="brand">Tide Rally</p>
    <p class="invite">Please join us for</p>
    <p class="goal">1000</p>
    <p class="goal-unit">LETTERS</p>
    <div class="tracker">
      <div class="tracker-fill"></div>
      <svg class="tracker-marker" viewBox="0 0 38 24" aria-hidden="true"><rect x="1" y="1" width="36" height="22" rx="1.5" fill="var(--envelope)" stroke="#c9ced8"/><path d="M1 2 L19 14 L37 2" fill="none" stroke="#c9ced8" stroke-width="1.2"/></svg>
      <span class="tracker-count">200</span>
    </div>
    <div class="star-band star-band--bottom" role="img" aria-label="Row of pale stars"></div>
  </section>

  <section class="panel panel--navy" style="--progress:28%">
    <div class="star-band star-band--top" role="img" aria-label="Row of muted stars"></div>
    <p class="brand">Tide Rally</p>
    <p class="invite">Please join us for</p>
    <p class="goal">1000</p>
    <p class="goal-unit">LETTERS</p>
    <div class="tracker">
      <div class="tracker-fill"></div>
      <svg class="tracker-marker" viewBox="0 0 38 24" aria-hidden="true"><rect x="1" y="1" width="36" height="22" rx="1.5" fill="var(--envelope)" stroke="#c9ced8"/><path d="M1 2 L19 14 L37 2" fill="none" stroke="#c9ced8" stroke-width="1.2"/></svg>
      <span class="tracker-count">300</span>
    </div>
    <div class="star-band star-band--bottom" role="img" aria-label="Row of muted stars"></div>
  </section>

  <section class="panel panel--sky" style="--progress:48%">
    <div class="star-band star-band--top" role="img" aria-label="Row of white stars"></div>
    <p class="brand">Tide Rally</p>
    <p class="invite">Please join us for</p>
    <p class="goal">1000</p>
    <p class="goal-unit">LETTERS</p>
    <div class="tracker">
      <div class="tracker-fill"></div>
      <svg class="tracker-marker" viewBox="0 0 38 24" aria-hidden="true"><rect x="1" y="1" width="36" height="22" rx="1.5" fill="var(--envelope)" stroke="#c9ced8"/><path d="M1 2 L19 14 L37 2" fill="none" stroke="#c9ced8" stroke-width="1.2"/></svg>
      <span class="tracker-count">500</span>
    </div>
    <div class="star-band star-band--bottom" role="img" aria-label="Row of white stars"></div>
  </section>

  <section class="panel panel--yellow" style="--progress:59%">
    <div class="star-band star-band--top" role="img" aria-label="Row of white stars"></div>
    <p class="brand">Tide Rally</p>
    <p class="invite">Please join us for</p>
    <p class="goal">1000</p>
    <p class="goal-unit">LETTERS</p>
    <div class="tracker">
      <div class="tracker-fill"></div>
      <svg class="tracker-marker" viewBox="0 0 38 24" aria-hidden="true"><rect x="1" y="1" width="36" height="22" rx="1.5" fill="var(--envelope)" stroke="#c9ced8"/><path d="M1 2 L19 14 L37 2" fill="none" stroke="#c9ced8" stroke-width="1.2"/></svg>
      <span class="tracker-count">660</span>
    </div>
    <div class="star-band star-band--bottom" role="img" aria-label="Row of white stars"></div>
  </section>

</main>
</body>
</html>
```